Fun Social App Need Simple, Logo, Clean App Design, and Icon

We need a app design for a new social meet up, planning app called Trimbly. The look and feel should be fun, yet clean and simple. This is an app for setting up meetings with friends and family. Our motto is Live Spontaneously. What we need:

-Logo

-App Icon

-Layout App pages as shown in attached. (Most will use the same header you come up with, with perhaps a few extras as you wish to add on each page)

-A button design that can be used throughout the app that conveys "push me" We will use this button in several places and simply change the text on it.
Updates

https://plarvenhub.net/blog/58213-20-striking-samples-of-sparse-phone-ux-layout#k.7x2qwfzlemuby We like the minimalist look.

Target Market(s)

Ages 10-39 Primarily

Industry/Entity Type

Social

Font styles to use
Sans Serif

Colors

Designer to choose colors to be used in the design.

Requirements
Must have
• Would like to focus on the S in the logo/icon. A S with arrows at both tips would be good.

```html
<!DOCTYPE html>
<html lang="en">
<head>
<meta charset="utf-8">
<title>Trimbly – Log in</title>
<link href="https://fonts.googleapis.com/css2?family=Roboto+Condensed:wght@300;400;500&family=Arimo:wght@400&display=swap" rel="stylesheet">
<style>
  :root {
    --brand-red: #e8301a;
    --soft-coral: #f8a293;
    --cancel-coral: #fa9481;
    --white: #ffffff;
    --label-grey: #555555;
    --divider: #e6e6e6;
  }
  * { margin: 0; padding: 0; box-sizing: border-box; }
  html, body {
    width: 676px;
    height: 1200px;
    overflow: hidden;
    background: var(--brand-red);
  }
  .login-screen {
    position: relative;
    width: 676px;
    height: 1200px;
    background: var(--brand-red);
    font-family: "Roboto Condensed", "Arial Narrow", sans-serif;
  }
  .brand {
    position: absolute;
    top: 131px;
    left: 0;
    width: 676px;
    height: 60px;
    display: flex;
    align-items: center;
    justify-content: center;
    gap: 14px;
  }
  .brand-dot {
    width: 26px;
    height: 26px;
    border-radius: 50%;
    background: var(--white);
  }
  .brand-name {
    font-family: "Roboto Condensed", "Arial Narrow", sans-serif;
    font-weight: 400;
    font-size: 46px;
    color: var(--white);
    line-height: 1;
  }
  .intro {
    position: absolute;
    top: 248px;
    left: 0;
    width: 676px;
    text-align: center;
    font-weight: 300;
    font-size: 31px;
    color: var(--soft-coral);
  }
  .credentials {
    position: absolute;
    top: 322px;
    left: 0;
    width: 676px;
    height: 208px;
    background: var(--white);
  }
  .field {
    position: absolute;
    left: 29px;
    font-family: "Arimo", Arial, sans-serif;
    font-size: 23px;
    color: var(--label-grey);
  }
  .field-email { top: 38px; }
  .field-password { top: 142px; }
  .field-divider {
    position: absolute;
    top: 104px;
    left: 34px;
    width: 608px;
    height: 1px;
    background: var(--divider);
  }
  .button {
    position: absolute;
    display: flex;
    align-items: center;
    justify-content: center;
    font-weight: 500;
    font-size: 39px;
    border-radius: 6px;
  }
  .button-login {
    top: 572px;
    left: 106px;
    width: 465px;
    height: 85px;
    background: var(--white);
    color: var(--brand-red);
  }
  .button-cancel {
    top: 679px;
    left: 104px;
    width: 469px;
    height: 87px;
    border: 1px solid var(--cancel-coral);
    color: var(--cancel-coral);
  }
  .forgot-link {
    position: absolute;
    top: 781px;
    left: 0;
    width: 676px;
    text-align: center;
    font-weight: 300;
    font-size: 29px;
    color: var(--white);
  }
</style>
</head>
<body>
  <main class="login-screen">
    <div class="brand">
      <span class="brand-dot"></span>
      <span class="brand-name">Trimbly</span>
    </div>
    <p class="intro">Log in with your trimbly account</p>

    <section class="credentials">
      <span class="field field-email">Email</span>
      <span class="field-divider"></span>
      <span class="field field-password">Password</span>
    </section>

    <div class="button button-login">Login</div>
    <div class="button button-cancel">Cancel</div>
    <p class="forgot-link">Forgot your password?</p>
  </main>
</body>
</html>
```